依頼詳細

他は、色、文字等、自由にデザインしていただき結構です。

記載項目
ロゴ、マップ、ショップインフォ、メニュー一部(初回お試し 100本¥5250・2回目以降120本 ¥6300)ミレナ ¥315
サイズ
B1
ページ数
片面
希望イメージ
シンプル 複雑
単色 カラフル
暗い 明るい
日常 高級
遊び心 厳粛
未来的 伝統的
女性的 男性的
希望する色
特になし
納品ファイル
• 高解像度JPG (.jpg)
• イラストレーター形式 (.ai)
補足説明
現在制作途中ですが仮サイト
http://www.kvr-m-mnsalon.kvr-web218.example/
です。
写真画像、いくつかアップします。(使用してもしなくてもどちらでも結構です。)
ロゴ
写真は使ってもどちらでも構いませんが、店内等いくつかアップします。
写真画像アップします。

夏らしくさわやか

皆様、たくさんのご提案いただきましてありがとうございました!

またよろしくおねがいいたします。

```html
<!DOCTYPE html>
<html lang="ja">
<head>
<meta charset="utf-8">
<title>Cielo</title>
<link href="https://fonts.googleapis.com/css2?family=Noto+Sans+JP:wght@300;400;500;700&display=swap" rel="stylesheet">
<style>
:root{
  --paper:#ffffff;
  --ink:#5a5a52;
  --olive:#a9b86a;
  --olive-dark:#8d9c50;
  --beige:#c9b48a;
  --muted:#8a8a80;
  --accent:#d86f7e;
  --photo-warm:#f3d7b8;
  --photo-light:#fbf1e6;
  --map-bg:#f4f2ea;
}
*{margin:0;padding:0;box-sizing:border-box}
html,body{width:851px;height:1200px;overflow:hidden;background:var(--paper)}
body{font-family:"Noto Sans JP",sans-serif;color:var(--ink);position:relative}
.hero-photo{position:absolute;left:230px;top:0;width:621px;height:440px;
  background:radial-gradient(ellipse at 45% 40%,var(--photo-warm) 0%,var(--photo-light) 55%,var(--paper) 85%)}
.catch{position:absolute;left:42px;top:38px;font-size:15px;line-height:1.5;letter-spacing:1px;color:var(--muted)}
.brand{position:absolute;left:42px;top:95px;width:150px;height:150px;border:2px solid var(--beige);border-radius:50%;
  display:flex;align-items:center;justify-content:center;font-size:28px;font-weight:500;letter-spacing:2px;color:var(--beige)}
.tagline{position:absolute;left:42px;top:262px;font-size:15px;color:var(--muted);letter-spacing:1px}
.headline{position:absolute;left:128px;top:440px;font-size:76px;font-weight:500;line-height:1.2;letter-spacing:2px;
  background:linear-gradient(90deg,#e86fa8,#f2a14a,#e6d24a,#8cc46a,#5cb6d8,#8a7fd0,#c47ac0);
  -webkit-background-clip:text;background-clip:text;color:transparent}
.menu{position:absolute;left:560px;top:715px;width:265px}
.menu-title{font-size:22px;font-weight:500;color:var(--olive-dark);letter-spacing:2px;border-bottom:1px solid var(--olive);padding-bottom:4px;margin-bottom:10px}
.menu-row{display:flex;justify-content:space-between;font-size:16px;line-height:2;color:var(--ink)}
.menu-row span:first-child{color:var(--accent)}
.info-band{position:absolute;left:0;top:912px;width:851px;height:46px;background:var(--olive);color:#fff;display:flex;align-items:center}
.tel{margin-left:30px;font-size:26px;font-weight:500;letter-spacing:1px}
.access{margin-left:auto;margin-right:250px;font-size:18px;letter-spacing:2px}
.hours{position:absolute;left:30px;top:966px;font-size:14px;line-height:1.6}
.site{position:absolute;left:30px;top:1016px;font-size:12px;color:var(--muted)}
.shop-photo{position:absolute;left:185px;top:1040px;width:90px;height:70px;background:linear-gradient(135deg,#e7dccb,#c9b99f)}
.note{position:absolute;left:30px;top:1130px;width:400px;font-size:11px;line-height:1.6;color:var(--muted)}
.map{position:absolute;left:455px;top:968px;width:370px;height:160px}
.address{position:absolute;left:455px;top:1140px;width:370px;font-size:10px;line-height:1.6;color:var(--muted)}
</style>
</head>
<body>
<div class="hero-photo" role="img" aria-label="まつげエクステをした女性のやわらかな肖像写真"></div>
<p class="catch">安心・安全の<br>まつげエクステ専用サロン</p>
<div class="brand">Cielo</div>
<p class="tagline">ワンランク上の上質な空間と癒しを</p>
<h1 class="headline">まつげ<br>もっと魅力的に。</h1>
<section class="menu">
  <h2 class="menu-title">MENU</h2>
  <div class="menu-row"><span>初回お試し</span><span>→ 100本 ¥5250</span></div>
  <div class="menu-row"><span>2回目以降</span><span>→ 120本 ¥6300</span></div>
  <div class="menu-row"><span>ミレナ</span><span>→ ¥315</span></div>
</section>
<div class="info-band">
  <span class="tel">TEL&amp;FAX 03-4127-9058</span>
  <span class="access">Access</span>
</div>
<p class="hours">営業時間 10:00〜19:00（最終受付 18:30）<br>定休 日・火曜日、祝祭日の第1月曜日</p>
<p class="site">http://www.kvr-m-mnsalon.kvr-web218.example/</p>
<div class="shop-photo" role="img" aria-label="サロン店内の写真"></div>
<p class="note">まつげエクステは 専任スタッフが 丁寧に 施術いたします。 ご予約は お電話にて 承ります。 お気軽に どうぞ。</p>
<svg class="map" viewBox="0 0 370 160" role="img" aria-label="サロン周辺の地図">
  <rect width="370" height="160" fill="var(--map-bg)"/>
</svg>
<p class="address">〒000-0000 東京都 中央区 みどり町 1-2-3 ハルビル 2F</p>
</body>
</html>
```